Quolvex custom business card design

Need a authentic, innovative business card design for a new mobile app business. I am uploading a few screen images from our app for you to view. I would like app design theme to match business card design. I can also send logo images.

```html
<!DOCTYPE html>
<html lang="en">
<head>
<meta charset="utf-8">
<title>Quolvex Business Card</title>
<link href="https://fonts.googleapis.com/css2?family=Montserrat:ital,wght@0,500;0,700;0,800;1,400&display=swap" rel="stylesheet">
<style>
  :root {
    --ink: #050706;
    --paper: #ffffff;
    --violet: #3a0fd6;
    --violet-deep: #16093f;
    --lilac: #8466ff;
    --mist: #e2e2e2;
    --edge: #6b6b6b;
  }
  html, body {
    margin: 0;
    padding: 0;
    width: 1200px;
    height: 735px;
    overflow: hidden;
    background: var(--paper);
  }
  .card {
    position: relative;
    width: 1200px;
    height: 735px;
    font-family: "Montserrat", sans-serif;
    color: var(--ink);
    overflow: hidden;
  }
  .card__art {
    position: absolute;
    inset: 0;
    width: 1200px;
    height: 735px;
  }
  .brand-name {
    position: absolute;
    left: 86px;
    top: 186px;
    transform: translateY(-50%);
    margin: 0;
    font-size: 68px;
    font-weight: 800;
    line-height: 1;
    color: var(--paper);
    letter-spacing: 0.5px;
  }
  .identity {
    position: absolute;
    left: 627px;
    width: 519px;
    top: 0;
  }
  .identity__name {
    position: absolute;
    left: 0;
    width: 100%;
    padding-left: 50px;
    box-sizing: border-box;
    top: 170px;
    transform: translateY(-50%);
    margin: 0;
    text-align: center;
    font-size: 58px;
    font-weight: 700;
    line-height: 1;
  }
  .identity__rule {
    position: absolute;
    left: 0;
    top: 196px;
    width: 519px;
    height: 2px;
    background: var(--ink);
  }
  .identity__tagline {
    position: absolute;
    left: 0;
    width: 100%;
    padding-left: 50px;
    box-sizing: border-box;
    top: 222px;
    transform: translateY(-50%);
    margin: 0;
    text-align: center;
    font-size: 27px;
    font-style: italic;
    font-weight: 400;
    line-height: 1;
  }
  .contacts {
    list-style: none;
    margin: 0;
    padding: 0;
  }
  .contacts__item {
    position: absolute;
    right: 111px;
    display: flex;
    align-items: center;
    gap: 16px;
    transform: translateY(-50%);
    font-size: 27px;
    font-weight: 700;
    line-height: 1;
    white-space: nowrap;
  }
  .contacts__icon {
    width: 53px;
    height: 53px;
    display: block;
  }
</style>
</head>
<body>
<main class="card">
  <svg class="card__art" viewBox="0 0 1066 653" aria-hidden="true">
    <defs>
      <linearGradient id="violet-fade" x1="0" y1="0" x2="1" y2="0">
        <stop offset="0" stop-color="var(--violet-deep)"/>
        <stop offset="1" stop-color="var(--violet)"/>
      </linearGradient>
    </defs>
    <rect class="backdrop" x="0" y="0" width="1066" height="653" fill="var(--ink)"/>
    <polygon class="backdrop__light" points="530,0 1018,0 1018,653 530,653 415,475 372,255" fill="var(--paper)"/>
    <polygon class="accent-top-deep" points="0,0 268,0 0,66" fill="var(--violet)"/>
    <polygon class="accent-top-soft" points="0,66 268,0 218,0 0,136" fill="var(--lilac)"/>
    <polygon class="accent-bottom" points="128,653 415,475 532,653" fill="url(#violet-fade)"/>
    <line class="lens-handle" x1="118" y1="655" x2="200" y2="520" stroke="var(--paper)" stroke-width="8"/>
    <circle class="lens-ring" cx="272" cy="388" r="154" fill="var(--paper)"/>
    <circle class="lens-face" cx="272" cy="388" r="140" fill="var(--mist)"/>
    <rect class="card-edge" x="0.5" y="0.5" width="1065" height="652" fill="none" stroke="var(--edge)" stroke-width="1"/>
  </svg>

  <h1 class="brand-name">Quolvex</h1>

  <section class="identity">
    <h2 class="identity__name">Your Name</h2>
    <div class="identity__rule"></div>
    <p class="identity__tagline">Your Tagline or Position here</p>
  </section>

  <ul class="contacts">
    <li class="contacts__item" style="top:391px">
      <span>+000 12345 875</span>
      <svg class="contacts__icon" viewBox="0 0 48 48" aria-label="Phone">
        <rect width="48" height="48" rx="7" fill="var(--violet)"/>
        <rect x="15" y="8" width="18" height="32" rx="3" fill="none" stroke="var(--paper)" stroke-width="2.5"/>
        <line x1="15" y1="34" x2="33" y2="34" stroke="var(--paper)" stroke-width="2"/>
        <circle cx="24" cy="37" r="1.3" fill="var(--paper)"/>
      </svg>
    </li>
    <li class="contacts__item" style="top:458px">
      <span>urwebiste.com</span>
      <svg class="contacts__icon" viewBox="0 0 48 48" aria-label="Website">
        <rect width="48" height="48" rx="7" fill="var(--violet)"/>
        <g fill="none" stroke="var(--paper)" stroke-width="2">
          <circle cx="24" cy="24" r="15"/>
          <ellipse cx="24" cy="24" rx="6.5" ry="15"/>
          <line x1="24" y1="9" x2="24" y2="39"/>
          <line x1="9" y1="24" x2="39" y2="24"/>
          <path d="M12 16 H36 M12 32 H36"/>
        </g>
      </svg>
    </li>
    <li class="contacts__item" style="top:524px">
      <span>ur@mailbox.com</span>
      <svg class="contacts__icon" viewBox="0 0 48 48" aria-label="Email">
        <rect width="48" height="48" rx="7" fill="var(--violet)"/>
        <rect x="8" y="13" width="32" height="22" rx="2" fill="none" stroke="var(--paper)" stroke-width="2.5"/>
        <path d="M9 15 L24 26 L39 15" fill="none" stroke="var(--paper)" stroke-width="2.5"/>
      </svg>
    </li>
    <li class="contacts__item" style="top:589px">
      <span>Street Address, 01 USA</span>
      <svg class="contacts__icon" viewBox="0 0 48 48" aria-label="Address">
        <rect width="48" height="48" rx="7" fill="var(--violet)"/>
        <path d="M24 39 C17 30 13 25 13 19 A11 11 0 0 1 35 19 C35 25 31 30 24 39 Z" fill="var(--paper)"/>
        <circle cx="24" cy="19" r="4.5" fill="var(--violet)"/>
      </svg>
    </li>
  </ul>
</main>
</body>
</html>
```